Livestock Consulting Company has a logo but needs business cards and a uniform logo

My company works with farmers advising them on managing cattle and sheep. I have a logo but need business cards and a version of my logo to go onto my work shirts. I need the following wording added to my logo for my shirts "Tallowby Livestock Consulting".

```html
<!DOCTYPE html>
<html lang="en">
<head>
<meta charset="utf-8">
<title>Tallowby Livestock Consulting – Business Cards</title>
<link rel="stylesheet" href="https://fonts.googleapis.com/css2?family=Montserrat:wght@500;600;800&display=swap">
<style>
  :root {
    --page: #efece6;
    --card: #ffffff;
    --brown: #7a6044;
    --brown-dark: #3b2a1a;
    --text: #3f3124;
  }
  * { box-sizing: border-box; margin: 0; padding: 0; }
  html, body { width: 900px; height: 1200px; overflow: hidden; }
  body {
    background: var(--page);
    font-family: "Montserrat", Arial, sans-serif;
    color: var(--text);
    position: relative;
  }
  .card {
    position: absolute;
    left: 124px;
    width: 651px;
    height: 380px;
    background: var(--card);
    overflow: hidden;
  }
  .card--front { top: 172px; }
  .card--back { top: 650px; }

  .arc { position: absolute; left: 0; width: 651px; }
  .arc--top { top: 0; }
  .arc--bottom { bottom: 0; }
  .arc path { fill: var(--brown); }

  .brand-name {
    position: absolute;
    text-align: center;
    font-weight: 800;
    color: var(--brown);
    text-transform: uppercase;
    line-height: 1.2;
    letter-spacing: 0.3px;
  }
  .card--front .brand-name {
    left: 20px; width: 294px; top: 158px;
    font-size: 19px;
  }
  .card--back .brand-name {
    left: 0; width: 651px; top: 156px;
    font-size: 28px;
  }

  .divider {
    position: absolute;
    left: 323px; top: 97px;
    width: 1px; height: 192px;
    background: var(--brown);
  }
  .contact { position: absolute; left: 341px; top: 92px; }
  .contact__name {
    font-weight: 600; font-size: 22px; color: var(--brown-dark);
    letter-spacing: 0.6px; line-height: 1.2;
  }
  .contact__title {
    font-weight: 600; font-size: 16px; color: var(--brown);
    letter-spacing: 0.4px; margin-top: 1px;
  }
  .contact__list { list-style: none; margin-top: 14px; }
  .contact__item {
    display: flex; align-items: flex-start;
    font-size: 14.5px; font-weight: 500; line-height: 22px;
  }
  .contact__item--address { margin-top: 11px; }
  .contact__icon {
    width: 17px; height: 17px; flex: none;
    margin: 2.5px 8px 0 0;
  }
  .contact__icon circle.bg { fill: var(--brown); }
  .contact__icon .glyph { fill: none; stroke: #fff; stroke-width: 1.3; stroke-linecap: round; stroke-linejoin: round; }
</style>
</head>
<body>

<section class="card card--front" aria-label="Business card front">
  <svg class="arc arc--top" viewBox="0 0 651 44" height="44" aria-hidden="true">
    <path d="M137 0 Q325 84 512 0 Z"/>
  </svg>

  <p class="brand-name">Tallowby Livestock<br>Consulting</p>

  <div class="divider"></div>

  <div class="contact">
    <h1 class="contact__name">WADE CARROW</h1>
    <p class="contact__title">CEO/FOUNDER</p>
    <ul class="contact__list">
      <li class="contact__item">
        <svg class="contact__icon" viewBox="0 0 17 17" aria-hidden="true"><circle class="bg" cx="8.5" cy="8.5" r="8.5"/><path class="glyph" d="M5.6 4.8l1.6-.4 1 2.2-1 .8q.9 1.8 2.6 2.6l.8-1 2.2 1-.4 1.6q-4.6.2-6.8-6.8z"/></svg>
        <span>555-014-2286</span>
      </li>
      <li class="contact__item">
        <svg class="contact__icon" viewBox="0 0 17 17" aria-hidden="true"><circle class="bg" cx="8.5" cy="8.5" r="8.5"/><rect class="glyph" x="4.3" y="5.5" width="8.4" height="6" rx="0.6"/><path class="glyph" d="M4.5 5.8l4 3.2 4-3.2"/></svg>
        <span>Wade@Tallowbyconsulting.com</span>
      </li>
      <li class="contact__item">
        <svg class="contact__icon" viewBox="0 0 17 17" aria-hidden="true"><circle class="bg" cx="8.5" cy="8.5" r="8.5"/><circle class="glyph" cx="8.5" cy="8.5" r="4.5"/><path class="glyph" d="M4 8.5h9M8.5 4q-2.6 4.5 0 9M8.5 4q2.6 4.5 0 9"/></svg>
        <span>www.Tallowbyconsulting.com</span>
      </li>
      <li class="contact__item contact__item--address">
        <svg class="contact__icon" viewBox="0 0 17 17" aria-hidden="true"><circle class="bg" cx="8.5" cy="8.5" r="8.5"/><path class="glyph" d="M8.5 13.2q-3.6-3.8-3.6-6a3.6 3.6 0 0 1 7.2 0q0 2.2-3.6 6z"/><circle class="glyph" cx="8.5" cy="7.2" r="1.3"/></svg>
        <span>118 Birchfield Road<br>Suite 12, Millbrook<br>MI 49021</span>
      </li>
    </ul>
  </div>

  <svg class="arc arc--bottom" viewBox="0 0 651 40" height="40" aria-hidden="true">
    <path d="M144 40 Q324 -36 504 40 Z"/>
  </svg>
</section>

<section class="card card--back" aria-label="Business card back">
  <p class="brand-name">Tallowby Livestock<br>Consulting</p>
</section>

</body>
</html>
```